Business card, postcard, pocket folder

We are a real estate team and have had a new logo designed. From this, we need the following deliverables:- Business Cards (double-sided)- Just Listed / Just Sold Postcards (double-sided)- Pocket Folder. See logo attached.More work possible for the winning designer.
There are 5 members of the team, so head shots should be easily changed and possible for a group photo might be a good idea for the pocket folder but not 100% neccessary.
Target Market(s)
Real estate
Industry/Entity Type
Real Estate
Font styles to use
Serif
Sans Serif
Requirements
Must have
- Business cards and postcards must have a head shot on them.

```html
<!DOCTYPE html>
<html lang="en">
<head>
<meta charset="utf-8">
<title>Harlowe Group – Print Collateral</title>
<link rel="stylesheet" href="https://fonts.googleapis.com/css2?family=Open+Sans:wght@400;600;700&display=swap">
<style>
:root{
  --blue:#22409a;
  --red:#e4171f;
  --ink:#2a2a2a;
  --paper:#ffffff;
  --bg:#e4e4e4;
  --sky1:#5b8fd1;
  --sky2:#c9d9ea;
}
*{box-sizing:border-box;margin:0;padding:0}
html,body{width:1200px;height:1200px;overflow:hidden;background:var(--bg);font-family:"Open Sans",sans-serif;color:var(--ink)}
.sheet{position:absolute;background:var(--paper);box-shadow:0 2px 8px rgba(0,0,0,.18)}

.brand{color:var(--blue);font-weight:600;letter-spacing:.5px;white-space:nowrap}

.contact{display:flex;align-items:stretch;gap:10px}
.contact-pill{background:var(--red);border-radius:999px;display:flex;flex-direction:column;justify-content:space-around;align-items:center;padding:4px 0}
.contact-pill svg{display:block}
.contact-lines{display:flex;flex-direction:column;justify-content:space-around;white-space:nowrap}

/* postcard front */
.postcard-front{left:60px;top:40px;width:500px;height:290px}
.pf-photo{position:absolute;left:14px;top:14px;width:472px;height:176px;background:linear-gradient(180deg,var(--sky1) 0%,var(--sky2) 45%,#b89a78 70%,#6d7f46 100%)}
.pf-brand{position:absolute;left:18px;top:24px;font-size:15px}
.pf-band{position:absolute;left:0;right:0;bottom:0;height:28px;background:var(--blue);color:#fff;display:flex;align-items:center;justify-content:space-between;padding:0 14px}
.pf-band .q{font-size:9.5px;font-weight:600}
.pf-band .ph{font-size:14px;font-weight:600;letter-spacing:.5px}
.pf-contact{position:absolute;left:28px;top:206px;height:68px;font-size:10px}
.pf-contact .contact-pill{width:16px}
.pf-team{position:absolute;right:22px;top:200px;width:140px;height:86px;background:linear-gradient(90deg,#5a5550,#9b9184 50%,#c9bca8)}

/* postcard back */
.postcard-back{left:60px;top:350px;width:500px;height:290px;padding:20px 22px;overflow:hidden}
.listings{display:grid;grid-template-columns:repeat(3,1fr);gap:18px 16px}
.listing{position:relative;font-size:6.5px;line-height:1.3}
.l-thumb{height:60px;background:linear-gradient(180deg,#7aa7dc 0%,#cfdde9 45%,#a68c6c 70%,#5f7a3c 100%);margin-bottom:5px}
.l-tag{position:absolute;left:-10px;top:8px;background:var(--red);color:#fff;font-size:8px;padding:2px 14px;transform:rotate(-30deg);transform-origin:left top}
.l-title{color:var(--red);font-weight:700;font-size:8.5px;margin-bottom:1px}
.l-meta{display:flex;gap:12px;margin-top:3px;align-items:center}
.l-meta span{display:flex;align-items:center;gap:3px}

/* folder */
.folder{position:absolute;left:600px;top:40px;width:560px;height:600px}
.folder-face{position:absolute;left:30px;top:0;width:500px;height:590px;background:var(--paper);box-shadow:0 2px 8px rgba(0,0,0,.18)}
.folder-brand{position:absolute;right:40px;top:190px;font-size:34px}
.folder-contact{position:absolute;left:14px;top:378px;height:50px;font-size:7px}
.folder-contact .contact-pill{width:8px;padding:2px 0}
.folder-pockets{position:absolute;left:0;bottom:0}

/* business cards */
.card{width:525px;height:300px;top:690px}
.card-front{left:60px;display:flex;align-items:center;justify-content:center}
.card-front .brand{font-size:42px}
.card-back{left:615px}
.cb-name{position:absolute;left:28px;top:26px;color:var(--blue);font-weight:700;font-size:30px;letter-spacing:.5px}
.cb-role{position:absolute;left:28px;top:66px;font-size:17px;color:#333}
.cb-contact{position:absolute;left:28px;top:168px;height:110px;font-size:13px}
.cb-contact .contact-pill{width:28px}
.cb-team{position:absolute;right:14px;bottom:0;width:200px;height:200px;background:linear-gradient(90deg,#5a5550,#a49a8c 45%,#4a3a34 70%,#cfc3ae)}
</style>
</head>
<body>

<section class="sheet postcard-front">
  <div class="pf-photo" role="img" aria-label="Photo of a two-storey brick and stucco family house under a blue sky">
    <div class="pf-brand brand">Harlowe Group</div>
    <div class="pf-band">
      <span class="q">THINKING OF SELLING OR NEED SOME ADVICE? CALL US TODAY!</span>
      <span class="ph">555-014-2378</span>
    </div>
  </div>
  <div class="contact pf-contact">
    <div class="contact-pill">
      <svg width="8" height="8" viewBox="0 0 10 10"><path d="M5 1a3 3 0 0 1 3 3c0 2-3 5-3 5S2 6 2 4a3 3 0 0 1 3-3z" fill="none" stroke="#fff"/></svg>
      <svg width="8" height="8" viewBox="0 0 10 10"><path d="M2 1h2l1 2-1 1a5 5 0 0 0 2 2l1-1 2 1v2c-4 0-7-3-7-7z" fill="#fff"/></svg>
      <svg width="8" height="8" viewBox="0 0 10 10"><rect x="1" y="2" width="8" height="6" fill="none" stroke="#fff"/><path d="M1 2l4 3 4-3" fill="none" stroke="#fff"/></svg>
      <svg width="8" height="8" viewBox="0 0 10 10"><circle cx="5" cy="5" r="4" fill="none" stroke="#fff"/><path d="M1 5h8M5 1v8" stroke="#fff"/></svg>
    </div>
    <div class="contact-lines">
      <span>Suite 410 , Alder Lane 8, Zip code 2045 City, Country</span>
      <span>555-014-2378</span>
      <span>info@harlowegroup.com</span>
      <span>www.harlowegroup.com</span>
    </div>
  </div>
  <div class="pf-team" role="img" aria-label="Group photo of four team members in business suits"></div>
</section>

<section class="sheet postcard-back">
  <div class="listings">
    <article class="listing"><div class="l-thumb" role="img" aria-label="Photo of a brick family house"></div><span class="l-tag">Sold</span>
      <div class="l-title">48 Linden Court in Avery</div><p>Bright corner home with open plan living, new kitchen and a large garden.</p>
      <div class="l-meta"><span>▬ 6 Beds</span><span>⌐ 6 Baths</span></div></article>
    <article class="listing"><div class="l-thumb" role="img" aria-label="Photo of a grey craftsman house"></div><span class="l-tag">Sold</span>
      <div class="l-title">48 Linden Court in Avery</div><p>Bright corner home with open plan living, new kitchen and a large garden.</p>
      <div class="l-meta"><span>▬ 6 Beds</span><span>⌐ 6 Baths</span></div></article>
    <article class="listing"><div class="l-thumb" role="img" aria-label="Photo of a stone family house"></div><span class="l-tag">Sold</span>
      <div class="l-title">48 Linden Court in Avery</div><p>Bright corner home with open plan living, new kitchen and a large garden.</p>
      <div class="l-meta"><span>▬ 6 Beds</span><span>⌐ 6 Baths</span></div></article>
    <article class="listing"><div class="l-thumb" role="img" aria-label="Photo of a brick family house"></div><span class="l-tag">Listed</span>
      <div class="l-title">48 Linden Court in Avery</div><p>Bright corner home with open plan living, new kitchen and a large garden.</p>
      <div class="l-meta"><span>▬ 6 Beds</span><span>⌐ 6 Baths</span></div></article>
    <article class="listing"><div class="l-thumb" role="img" aria-label="Photo of a grey craftsman house"></div><span class="l-tag">Listed</span>
      <div class="l-title">48 Linden Court in Avery</div><p>Bright corner home with open plan living, new kitchen and a large garden.</p>
      <div class="l-meta"><span>▬ 6 Beds</span><span>⌐ 6 Baths</span></div></article>
    <article class="listing"><div class="l-thumb" role="img" aria-label="Photo of a stone family house"></div><span class="l-tag">Listed</span>
      <div class="l-title">48 Linden Court in Avery</div><p>Bright corner home with open plan living, new kitchen and a large garden.</p>
      <div class="l-meta"><span>▬ 6 Beds</span><span>⌐ 6 Baths</span></div></article>
  </div>
</section>

<section class="folder">
  <svg class="folder-flaps" width="560" height="600" style="position:absolute;left:0;top:0">
    <path d="M30 300 L0 312 L0 430 L30 442 Z" fill="var(--blue)"/>
    <path d="M530 300 L560 312 L560 430 L530 442 Z" fill="var(--blue)"/>
  </svg>
  <div class="folder-face">
    <div class="folder-brand brand">Harlowe Group</div>
    <div class="contact folder-contact">
      <div class="contact-pill"></div>
      <div class="contact-lines">
        <span>Suite 410 , Alder Lane 8, Zip code 2045</span>
        <span>City, Country</span>
        <span>555-014-2378</span>
        <span>info@harlowegroup.com</span>
        <span>www.harlowegroup.com</span>
      </div>
    </div>
    <svg class="folder-pockets" width="500" height="150" viewBox="0 0 500 150">
      <path d="M0 0 H264 L257 136 Q256 150 242 150 H0 Z" fill="var(--blue)"/>
      <path d="M267 0 H500 V150 H290 Q276 150 275 136 Z" fill="var(--blue)"/>
    </svg>
  </div>
</section>

<section class="sheet card card-front">
  <div class="brand">Harlowe Group</div>
</section>

<section class="sheet card card-back">
  <h1 class="cb-name">DANA REYES</h1>
  <p class="cb-role">Chief Executive</p>
  <div class="contact cb-contact">
    <div class="contact-pill">
      <svg width="16" height="16" viewBox="0 0 10 10"><path d="M5 1a3 3 0 0 1 3 3c0 2-3 5-3 5S2 6 2 4a3 3 0 0 1 3-3z" fill="none" stroke="#fff" stroke-width=".8"/></svg>
      <svg width="16" height="16" viewBox="0 0 10 10"><path d="M2 1h2l1 2-1 1a5 5 0 0 0 2 2l1-1 2 1v2c-4 0-7-3-7-7z" fill="#fff"/></svg>
      <svg width="16" height="16" viewBox="0 0 10 10"><rect x="1" y="2" width="8" height="6" fill="none" stroke="#fff" stroke-width=".8"/><path d="M1 2l4 3 4-3" fill="none" stroke="#fff" stroke-width=".8"/></svg>
      <svg width="16" height="16" viewBox="0 0 10 10"><circle cx="5" cy="5" r="4" fill="none" stroke="#fff" stroke-width=".8"/><path d="M1 5h8M5 1v8" stroke="#fff" stroke-width=".8"/></svg>
    </div>
    <div class="contact-lines">
      <span>Suite 410 , Alder Lane 8, Zip code<br>City, Country</span>
      <span>555-014-2378</span>
      <span>info@harlowegroup.com</span>
      <span>www.harlowegroup.com</span>
    </div>
  </div>
  <div class="cb-team" role="img" aria-label="Group photo of four team members in business suits"></div>
</section>

</body>
</html>
```